Business Card Design/Logo

I require a design/logo for my own Company, Morvix. The Jewellery I make is totally hand crafted. I own a hand Mining Claim out in the gemfields of Queensland and dig up my own stones. I also fossick for Gold Locally so all my Jewellery products are hand dug/cut/created. Quality stones are hand cut by my partner (Faceted) and other stones (Seconds) are either skin polished or recessed into pieces of Solid 925 Silver or Solid 9ct and 18 ct Gold. I make Sets (Collections) or just one-of designs. All the stones come in different colours and I am now starting to use different colour Golds. The final design should radiate professionalism, quality and uniqueness.

Target Market(s)

Many designs will cost a minimum of AU Dollars $2,000

Industry/Entity Type

Business

Contact Information for Business Card

Morvix Creations
Distinct Bench Wrought Native Adornments
0400327986
P.O. Box 418 Ambercrest 4719 Qld
morvixgarnets@mailbrook.net

```html
<!DOCTYPE html>
<html lang="en">
<head>
<meta charset="utf-8">
<title>Morvix Creations – Business Card</title>
<link rel="stylesheet" href="https://fonts.googleapis.com/css2?family=Quicksand:wght@400;500;600&display=swap">
<style>
  :root {
    --stage: #ece8e3;
    --orange-deep: #c8401c;
    --orange-mid: #e2612c;
    --orange-light: #f08a4f;
    --panel: rgba(255, 190, 140, 0.22);
    --white: #ffffff;
    --brand: #8c7b6b;
    --tagline: #d2454a;
    --contact: #fff4ec;
  }
  * { margin: 0; padding: 0; box-sizing: border-box; }
  html, body {
    width: 1200px;
    height: 1023px;
    overflow: hidden;
    background: var(--stage);
    font-family: "Quicksand", sans-serif;
  }
  .canvas {
    position: relative;
    width: 1200px;
    height: 1023px;
  }
  .card {
    position: absolute;
    left: 150px;
    top: 254px;
    width: 900px;
    height: 514px;
    border-radius: 6px;
    overflow: hidden;
    background: radial-gradient(ellipse at 45% 40%, var(--orange-light) 0%, var(--orange-mid) 45%, var(--orange-deep) 100%);
    box-shadow: 0 18px 40px rgba(60, 40, 20, 0.25);
  }
  .card__curve {
    position: absolute;
    inset: 0;
    width: 900px;
    height: 514px;
  }
  .brand {
    position: absolute;
    left: 56px;
    top: 300px;
    display: flex;
    align-items: center;
    gap: 12px;
    white-space: nowrap;
  }
  .brand__dot {
    width: 16px;
    height: 16px;
    border-radius: 50%;
    background: var(--orange-mid);
  }
  .brand__name {
    font-size: 34px;
    font-weight: 500;
    color: var(--brand);
    letter-spacing: 0.5px;
  }
  .tagline {
    position: absolute;
    left: 56px;
    top: 362px;
    font-size: 16px;
    font-weight: 600;
    color: var(--tagline);
    letter-spacing: 0.3px;
    white-space: nowrap;
  }
  .contact-panel {
    position: absolute;
    left: 500px;
    top: 70px;
    width: 370px;
    height: 300px;
    border-radius: 28px;
    background: var(--panel);
  }
  .necklace-art {
    position: absolute;
    left: 560px;
    top: 40px;
    width: 250px;
    height: 90px;
    border-radius: 0 0 125px 125px;
    background: linear-gradient(180deg, rgba(255, 220, 200, 0.15), rgba(255, 225, 205, 0.45));
  }
  .contact-list {
    position: absolute;
    left: 526px;
    top: 170px;
    width: 330px;
    list-style: none;
    color: var(--contact);
    font-size: 17px;
    font-weight: 500;
  }
  .contact-list li {
    display: flex;
    align-items: center;
    gap: 12px;
    margin-bottom: 22px;
    white-space: nowrap;
  }
  .contact-list svg { width: 18px; height: 18px; flex: none; }
</style>
</head>
<body>
  <main class="canvas">
    <section class="card" aria-label="Morvix Creations business card">
      <svg class="card__curve" viewBox="0 0 900 514" aria-hidden="true">
        <path d="M0 150 Q 300 120 440 300 Q 500 400 470 514 L0 514 Z" fill="var(--white)"/>
      </svg>

      <div class="brand">
        <span class="brand__dot"></span>
        <span class="brand__name">Morvix Creations</span>
      </div>
      <p class="tagline">Bench Wrought Native Adornments</p>

      <div class="contact-panel"></div>
      <div class="necklace-art" role="img" aria-label="Faint illustration of a gemstone necklace"></div>

      <ul class="contact-list">
        <li>
          <svg viewBox="0 0 18 18"><rect x="4" y="1" width="10" height="16" rx="2" fill="none" stroke="currentColor" stroke-width="1.6"/><circle cx="9" cy="14" r="1" fill="currentColor"/></svg>
          0400327986
        </li>
        <li>
          <svg viewBox="0 0 18 18"><rect x="1" y="3.5" width="16" height="11" rx="1.5" fill="none" stroke="currentColor" stroke-width="1.6"/><path d="M1.5 4.5 L9 10 L16.5 4.5" fill="none" stroke="currentColor" stroke-width="1.6"/></svg>
          morvixgarnets@mailbrook.net
        </li>
        <li>
          <svg viewBox="0 0 18 18"><path d="M9 17 C4 11 3 9 3 7 A6 6 0 0 1 15 7 C15 9 14 11 9 17 Z" fill="currentColor"/><circle cx="9" cy="7" r="2.2" fill="var(--orange-mid)"/></svg>
          P.O. Box 418 Ambercrest 4719 Qld
        </li>
      </ul>
    </section>
  </main>
</body>
</html>
```